Vextor General Painting Ltd. - Construction painting company providing high-quality service

We need a logo and business card design for a painting company that provides high-quality work for major developers and builders in Calgary, Alberta. Our projects include commercial high-rise residential towers. We would like designs that communicate professionalism and high quality service.
Target Market(s)
Developers and builders
Industry/Entity Type
Construction
Contact Information for Business Card
Company name, employee name, title, phone number, email address
Colors
Designer to choose colors to be used in the design.
Look and feel
Each slider illustrates characteristics of the customer's brand and the style your logo design should communicate.

```html
<!DOCTYPE html>
<html lang="en">
<head>
<meta charset="UTF-8">
<title>Vextor General Painting Ltd. – Business Card</title>
<link rel="stylesheet" href="https://fonts.googleapis.com/css2?family=Montserrat:wght@500;700&family=Lato:wght@400;700&display=swap">
<style>
  :root {
    --stage: #2a2a2a;
    --ink: #000000;
    --brand-red: #ff0000;
    --paper: #ffffff;
    --card-w: 700px;
    --card-h: 400px;
  }
  * { box-sizing: border-box; margin: 0; padding: 0; }
  html, body {
    width: 1200px; height: 1015px; overflow: hidden;
    background: var(--stage);
  }
  .stage {
    width: 1200px; height: 1015px;
    display: flex; flex-direction: column; align-items: center; justify-content: center;
    gap: 60px;
  }
  .card {
    position: relative;
    width: var(--card-w); height: var(--card-h);
    overflow: hidden;
    box-shadow: 0 18px 40px rgba(0,0,0,0.55);
  }
  .card-back { background: var(--ink); }
  .card-front { background: var(--brand-red); }
  .card-shape { position: absolute; inset: 0; }

  .wordmark {
    position: absolute;
    display: flex; flex-direction: column; align-items: center;
    font-family: 'Montserrat', sans-serif; font-weight: 700;
    color: var(--brand-red); text-transform: uppercase; line-height: 1.1;
    white-space: nowrap;
  }
  .wordmark-badge {
    width: 90px; height: 90px; border-radius: 50%;
    border: 5px solid var(--brand-red); margin-bottom: 16px;
  }
  .wordmark-name { font-size: 46px; letter-spacing: 8px; }
  .wordmark-sub { font-size: 15px; letter-spacing: 3px; margin-top: 6px; }
  .card-back .wordmark { left: 0; right: 0; top: 80px; }
  .card-front .wordmark { left: 450px; width: 260px; top: 55px; }
  .card-front .wordmark-name { font-size: 40px; letter-spacing: 6px; }
  .card-front .wordmark-sub { font-size: 13px; letter-spacing: 2px; }

  .holder {
    position: absolute; left: 56px; top: 152px;
    color: var(--paper); white-space: nowrap;
  }
  .holder-name {
    font-family: 'Montserrat', sans-serif; font-weight: 700;
    font-size: 25px; letter-spacing: 0;
  }
  .holder-title {
    font-family: 'Lato', sans-serif; font-weight: 400;
    font-size: 20px; margin-top: 2px;
  }
  .contacts {
    position: absolute; left: 56px; top: 268px;
    list-style: none; color: var(--paper);
    font-family: 'Lato', sans-serif; font-size: 18px;
  }
  .contacts li { display: flex; align-items: center; gap: 10px; height: 28px; }
  .contacts svg { width: 18px; height: 18px; flex: none; }
</style>
</head>
<body>
<main class="stage">
  <section class="card card-back" aria-label="Card back">
    <div class="wordmark">
      <span class="wordmark-badge"></span>
      <span class="wordmark-name">Vextor</span>
      <span class="wordmark-sub">General Painting Ltd.</span>
    </div>
  </section>

  <section class="card card-front" aria-label="Card front">
    <svg class="card-shape" viewBox="0 0 700 400" aria-hidden="true">
      <circle cx="572" cy="140" r="256" fill="var(--ink)"/>
      <circle cx="584" cy="140" r="250" fill="var(--paper)"/>
    </svg>

    <div class="wordmark">
      <span class="wordmark-badge"></span>
      <span class="wordmark-name">Vextor</span>
      <span class="wordmark-sub">General Painting Ltd.</span>
    </div>

    <div class="holder">
      <p class="holder-name">DANIEL MORROW</p>
      <p class="holder-title">Managing Director</p>
    </div>

    <ul class="contacts">
      <li>
        <svg viewBox="0 0 24 24" fill="none" stroke="currentColor" stroke-width="2"><path d="M5 3h4l2 5-2.5 1.5a11 11 0 0 0 6 6L16 13l5 2v4a2 2 0 0 1-2 2A16 16 0 0 1 3 5a2 2 0 0 1 2-2z"/></svg>
        044-987 654 321
      </li>
      <li>
        <svg viewBox="0 0 24 24" fill="none" stroke="currentColor" stroke-width="2"><rect x="2" y="5" width="20" height="14"/><path d="M2 5l10 8 10-8"/></svg>
        info@vextorpainting.com
      </li>
      <li>
        <svg viewBox="0 0 24 24" fill="none" stroke="currentColor" stroke-width="2"><circle cx="12" cy="12" r="10"/><path d="M2 12h20M12 2a15 15 0 0 1 0 20M12 2a15 15 0 0 0 0 20"/></svg>
        www.vextorpainting.com
      </li>
    </ul>
  </section>
</main>
</body>
</html>
```